Group Medical Practice needs stationery, business cards etc. designed

We need stationery designed for a multisite practice that offers primary medical, dental and behavioral healthcare. We would like a design that is consistent for letterhead, business cards, Microsoft Outlook stationery etc. We have attached our new logo design.

Business

```html
<!DOCTYPE html>
<html lang="en">
<head>
<meta charset="utf-8">
<title>Cedar Ridge Care Group – Stationery</title>
<link rel="stylesheet" href="https://fonts.googleapis.com/css2?family=Open+Sans:wght@400;600&family=Play&display=swap">
<style>
  :root {
    --backdrop: #9c9e9d;
    --leaf: #8cc63f;
    --ink-blue: #0f6db7;
    --paper: #ffffff;
    --text: #1e1e1e;
    --rule: #8a8a8a;
  }
  * { box-sizing: border-box; margin: 0; padding: 0; }
  html, body { width: 1200px; height: 1000px; overflow: hidden; }
  body {
    background: var(--backdrop);
    position: relative;
    font-family: "Open Sans", Arial, sans-serif;
    color: var(--text);
  }
  .card {
    position: absolute;
    left: 24px;
    width: 376px;
    height: 214px;
    box-shadow: 2px 3px 4px rgba(0,0,0,0.35);
    overflow: hidden;
  }
  .card--green { background: var(--leaf); color: #fff; }
  .card--white { background: var(--paper); }
  .card--front-green { top: 32px; }
  .card--front-white { top: 274px; }
  .card--back-white { top: 518px; }
  .card--back-green { top: 760px; }

  .holder { position: absolute; right: 18px; top: 62px; text-align: right; }
  .holder__name { font-family: "Play", sans-serif; font-size: 15px; line-height: 20px; letter-spacing: 0.3px; }
  .holder__role { font-size: 10px; line-height: 14px; margin-top: 4px; }
  .card--front-white .holder__name { color: var(--leaf); }
  .holder__rule { position: absolute; left: 0; width: 310px; height: 1px; top: 93px; }
  .card--front-green .holder__rule { background: rgba(255,255,255,0.8); }
  .card--front-white .holder__rule { background: var(--rule); }

  .contact { position: absolute; left: 18px; top: 103px; font-size: 10.5px; line-height: 17px; }
  .contact__row { display: flex; align-items: center; gap: 7px; }
  .contact__row svg { width: 11px; height: 11px; }
  .contact__address { margin-top: 4px; line-height: 13px; font-size: 10px; }
  .card--front-white .contact__row svg { fill: var(--leaf); }
  .card--front-green .contact__row svg { fill: #fff; }

  .brand {
    position: absolute; left: 0; right: 0; top: 0; bottom: 0;
    display: flex; align-items: center; justify-content: center;
    font-size: 26px; font-weight: 600; color: var(--ink-blue); letter-spacing: 0.5px;
  }

  .letterhead {
    position: absolute; left: 540px; top: 96px; width: 560px; height: 792px;
    background: var(--paper);
    box-shadow: 3px 4px 0 #e6e6e6, 6px 8px 0 var(--leaf), 8px 10px 8px rgba(0,0,0,0.35);
    overflow: hidden;
  }
  .letterhead__brand {
    position: absolute; left: 36px; top: 46px;
    font-size: 19px; font-weight: 600; color: var(--ink-blue);
  }
  .letterhead__contact {
    position: absolute; right: 30px; top: 40px;
    display: flex; gap: 8px; font-size: 8px; line-height: 11px;
  }
  .letterhead__address { text-align: right; padding-top: 8px; }
  .letterhead__divider { width: 1px; background: var(--rule); }
  .letterhead__lines .contact__row { gap: 5px; }
  .letterhead__lines svg { width: 8px; height: 8px; fill: var(--leaf); }
  .letterhead__footer { position: absolute; left: 0; bottom: 0; width: 560px; height: 170px; }
</style>
</head>
<body>
  <svg width="0" height="0" style="position:absolute">
    <defs>
      <symbol id="icon-phone" viewBox="0 0 12 12"><path d="M1 3c0-1 1-2 2-2h6c1 0 2 1 2 2v1H8V3H4v1H1zM2 5h8l1 5H1z"/></symbol>
      <symbol id="icon-web" viewBox="0 0 12 12"><path d="M6 0a6 6 0 1 0 0 12A6 6 0 0 0 6 0zm0 1.2c.7.8 1.2 2 1.3 3.3H4.7C4.8 3.2 5.3 2 6 1.2zM1.3 5.5h2.4c0 1 .2 2 .6 3.1A4.8 4.8 0 0 1 1.3 5.5zm0-1a4.8 4.8 0 0 1 3-3.1c-.4 1-.6 2-.6 3.1zm3.4 1h2.6c-.1 1.3-.6 2.5-1.3 3.3-.7-.8-1.2-2-1.3-3.3zm3.6 0h2.4a4.8 4.8 0 0 1-3 3.1c.4-1 .6-2 .6-3.1zm0-1c0-1-.2-2-.6-3.1a4.8 4.8 0 0 1 3 3.1z"/></symbol>
      <symbol id="icon-mail" viewBox="0 0 12 12"><path d="M0 2h12v8H0zm1 1v.4l5 3.2 5-3.2V3zm0 1.6V9h10V4.6L6 7.8z"/></symbol>
    </defs>
  </svg>

  <section class="card card--green card--front-green">
    <div class="holder"><div class="holder__name">Martin Hale</div><div class="holder__role">Director</div></div>
    <div class="holder__rule"></div>
    <div class="contact">
      <div class="contact__row"><svg><use href="#icon-phone"/></svg>1300 555 019</div>
      <div class="contact__row"><svg><use href="#icon-web"/></svg>www.cedarridgecare.com</div>
      <div class="contact__row"><svg><use href="#icon-mail"/></svg>hello@cedarridgecare.com</div>
      <div class="contact__address">24 Alder Lane, Northgate<br>Brookfield, 3192, Australia</div>
    </div>
  </section>

  <section class="card card--white card--front-white">
    <div class="holder"><div class="holder__name">Martin Hale</div><div class="holder__role">Director</div></div>
    <div class="holder__rule"></div>
    <div class="contact">
      <div class="contact__row"><svg><use href="#icon-phone"/></svg>1300 555 019</div>
      <div class="contact__row"><svg><use href="#icon-web"/></svg>www.cedarridgecare.com</div>
      <div class="contact__row"><svg><use href="#icon-mail"/></svg>hello@cedarridgecare.com</div>
      <div class="contact__address">24 Alder Lane, Northgate<br>Brookfield, 3192, Australia</div>
    </div>
  </section>

  <section class="card card--white card--back-white">
    <div class="brand">Cedar Ridge Care Group</div>
  </section>

  <section class="card card--green card--back-green">
    <div class="brand">Cedar Ridge Care Group</div>
  </section>

  <section class="letterhead">
    <div class="letterhead__brand">Cedar Ridge Care Group</div>
    <div class="letterhead__contact">
      <div class="letterhead__address">24 Alder Lane, Northgate<br>Brookfield, 3192, Australia</div>
      <div class="letterhead__divider"></div>
      <div class="letterhead__lines">
        <div class="contact__row"><svg><use href="#icon-phone"/></svg>1300 555 019</div>
        <div class="contact__row"><svg><use href="#icon-web"/></svg>www.cedarridgecare.com</div>
        <div class="contact__row"><svg><use href="#icon-mail"/></svg>hello@cedarridgecare.com</div>
      </div>
    </div>
    <svg class="letterhead__footer" viewBox="0 0 560 170" preserveAspectRatio="none">
      <path d="M0 30 C150 10 250 40 340 90 C400 122 450 128 490 126 L0 126 Z" fill="var(--ink-blue)"/>
      <path d="M0 44 C150 24 250 52 335 100 C390 130 440 138 490 134 C520 130 545 112 560 92 L560 170 L0 170 Z" fill="var(--leaf)"/>
    </svg>
  </section>
</body>
</html>
```